" A VORA SAN é uma empresa de engenharia especializada na manutençao de equipamentos biomédicos e no desenvolvimento de soluçoes para os diversos serviços de saúde "

```html
<!DOCTYPE html>
<html lang="pt">
<head>
<meta charset="utf-8">
<title>VORA SAN – Pasta institucional</title>
<link href="https://fonts.googleapis.com/css2?family=Montserrat:wght@400;600;700&display=swap" rel="stylesheet">
<style>
  :root {
    --backdrop: #ecebe8;
    --brand-red: #ee1c25;
    --brand-red-tint: #f23b42;
    --paper: #ffffff;
    --ink-grey: #6d6e71;
    --shadow: rgba(0,0,0,0.18);
  }
  * { box-sizing: border-box; margin: 0; padding: 0; }
  html, body {
    width: 1200px; height: 1200px; overflow: hidden;
    background: var(--backdrop);
    font-family: "Montserrat", sans-serif;
  }
  .folder {
    position: absolute; left: 115px; top: 100px;
    width: 970px; height: 1005px;
    filter: drop-shadow(0 6px 14px var(--shadow));
  }
  .cover-front {
    position: absolute; left: 0; top: 0;
    width: 485px; height: 850px;
    background: var(--brand-red);
    overflow: hidden;
  }
  .cover-back {
    position: absolute; left: 485px; top: 0;
    width: 485px; height: 1005px;
    background: var(--paper);
  }
  .pocket {
    position: absolute; left: 0; top: 850px;
    width: 485px; height: 155px;
  }
  .brand-disc-decor {
    position: absolute; left: 55px; top: 190px;
    width: 310px; height: 310px; border-radius: 50%;
    background: var(--brand-red-tint);
  }
  .brand {
    position: absolute; display: flex; align-items: center; gap: 10px;
    font-weight: 700; letter-spacing: 0.02em; white-space: nowrap;
  }
  .brand-dot { border-radius: 50%; flex: none; }
  .brand--back {
    left: 60px; top: 405px; flex-direction: column; align-items: flex-start; gap: 4px;
  }
  .brand--back .brand-row { display: flex; align-items: center; gap: 12px; }
  .brand--back .brand-dot { width: 44px; height: 44px; background: var(--ink-grey); }
  .brand--back .brand-name { font-size: 46px; color: var(--brand-red); line-height: 1; }
  .brand-tagline {
    margin-left: 56px; font-size: 12px; font-weight: 600;
    color: var(--ink-grey); letter-spacing: 0.12em;
  }
  .brand--front { left: 26px; top: 690px; }
  .brand--front .brand-dot { width: 18px; height: 18px; background: var(--paper); }
  .brand--front .brand-name { font-size: 18px; color: var(--paper); }
  .contact-lines {
    position: absolute; left: 26px; top: 722px;
    color: var(--paper); font-size: 7px; line-height: 1.7; font-weight: 400;
  }
  .brand--pocket {
    left: 40px; top: 925px; transform: rotate(180deg);
  }
  .brand--pocket .brand-dot { width: 26px; height: 26px; background: var(--ink-grey); }
  .brand--pocket .brand-name { font-size: 24px; color: var(--brand-red); }
</style>
</head>
<body>
  <main class="folder">
    <section class="cover-front">
      <div class="brand-disc-decor" role="img" aria-label="Símbolo da marca em grande escala, em vermelho claro"></div>
      <div class="brand brand--front">
        <span class="brand-dot"></span>
        <span class="brand-name">VORA SAN</span>
      </div>
      <p class="contact-lines">
        www.vorasan.com.br · contato@vorasan.com.br<br>
        Rua Alfa, 120 · Curitiba · (41) 3000-0000
      </p>
    </section>

    <section class="cover-back">
      <div class="brand brand--back">
        <div class="brand-row">
          <span class="brand-dot"></span>
          <span class="brand-name">VORA SAN</span>
        </div>
        <span class="brand-tagline">Engenharia Hospitalar</span>
      </div>
    </section>

    <svg class="pocket" viewBox="0 0 485 155" aria-hidden="true">
      <polygon points="0,0 470,0 485,12 445,155 0,155" fill="#ffffff"/>
      <line x1="0" y1="0.5" x2="470" y2="0.5" stroke="#d9d9d9" stroke-width="1"/>
    </svg>

    <div class="brand brand--pocket">
      <span class="brand-dot"></span>
      <span class="brand-name">VORA SAN</span>
    </div>
  </main>
</body>
</html>
```